Outdoor mass notification company needing business card design.

Our company name is Harrowgate Signal Systems Inc located in Amory Mississippi and we sell and maintain "Brantor" Mass Notification Sirens in the US. Outdoor sirens notify people of certain severe dangers such as tornados, severe thunderstorms, flooding, hurricanes and tsunamis. We also serve the oil and gas refining industries to warn of Chemical releases, fires, and lightning alerts.

Contact Information for Business Card

Name, title, cell number, email address

Requirements
Nice to have
• The Brantor logo and also the Mildvane logo.

```html
<!DOCTYPE html>
<html lang="en">
<head>
<meta charset="utf-8">
<title>Harrowgate Signal Systems – Business Card</title>
<link href="https://fonts.googleapis.com/css2?family=Arimo:wght@400;700&family=Tinos:wght@400;700&display=swap" rel="stylesheet">
<style>
  :root {
    --stage: #d9dadc;
    --navy: #2f4a66;
    --navy-text: #34506e;
    --white: #ffffff;
    --ink: #1e1e1e;
    --rule: #c9d3de;
    --card-edge: #b9bcc0;
    --img-light: #e6e7e8;
    --img-mid: #9a9c9f;
    --img-dark: #3b3d40;
  }
  * { box-sizing: border-box; margin: 0; padding: 0; }
  html, body { width: 1200px; height: 800px; overflow: hidden; }
  body {
    background: var(--stage);
    display: flex;
    align-items: center;
    justify-content: center;
    gap: 40px;
    font-family: "Arimo", Arial, sans-serif;
  }
  .card {
    position: relative;
    width: 540px;
    height: 310px;
    border-radius: 18px;
    overflow: hidden;
    box-shadow: 0 2px 6px rgba(0,0,0,.18);
  }

  /* Front */
  .card-front { background: var(--navy); color: var(--white); }
  .brand {
    position: absolute;
    left: 36px; top: 136px;
    width: 210px;
    display: flex; align-items: center; gap: 10px;
  }
  .brand-mark { width: 14px; height: 14px; background: var(--white); flex: none; }
  .brand-name {
    font-family: "Arimo", Arial, sans-serif;
    font-weight: 400;
    font-size: 16px;
    line-height: 1.25;
  }
  .divider {
    position: absolute;
    left: 262px; top: 78px;
    width: 1px; height: 160px;
    background: var(--rule);
  }
  .contact {
    position: absolute;
    left: 284px; top: 74px;
    font-size: 13px;
    line-height: 1.3;
  }
  .contact-name { font-size: 19px; font-weight: 700; }
  .contact-title { margin-bottom: 12px; }
  .contact-address { margin-bottom: 12px; }

  /* Back */
  .card-back { background: var(--white); color: var(--ink); border: 1px solid var(--card-edge); }
  .art { position: absolute; border-radius: 4px; }
  .art-tower { left: 190px; top: 18px; width: 150px; height: 118px;
    background: radial-gradient(circle at 50% 55%, var(--img-mid), var(--img-light) 75%); }
  .art-siren-array { left: 362px; top: 14px; width: 160px; height: 118px;
    background: linear-gradient(135deg, var(--img-light), var(--img-mid)); }
  .art-siren-pole { left: 22px; top: 160px; width: 38px; height: 100px;
    background: linear-gradient(180deg, var(--img-dark), var(--img-mid)); }
  .services {
    position: absolute;
    left: 70px; right: 20px; top: 148px;
    text-align: center;
  }
  .services-heading {
    font-family: "Tinos", "Times New Roman", serif;
    font-weight: 700;
    font-size: 19px;
    color: var(--navy-text);
    margin-bottom: 6px;
  }
  .services-lead { font-size: 16px; line-height: 1.2; }
  .services-list { font-size: 12.5px; line-height: 1.3; margin-bottom: 10px; }
  .sep { color: var(--navy-text); }
</style>
</head>
<body>

  <section class="card card-front" aria-label="Card front">
    <div class="brand">
      <span class="brand-mark"></span>
      <span class="brand-name">Harrowgate Signal Systems</span>
    </div>
    <div class="divider"></div>
    <div class="contact">
      <div class="contact-name">Martin Kessler</div>
      <div class="contact-title">President</div>
      <div class="contact-address">412 Cedar Bend Road<br>Amory, MS 38821</div>
      <div>(662) 555-0148</div>
      <div>name@harrowgatesignal.com</div>
      <div>www.harrowgatesignal.com</div>
    </div>
  </section>

  <section class="card card-back" aria-label="Card back">
    <div class="art art-tower" role="img" aria-label="Grey illustration of a radio tower sending signal bolts"></div>
    <div class="art art-siren-array" role="img" aria-label="Photo of a rotating outdoor siren with horn array"></div>
    <div class="art art-siren-pole" role="img" aria-label="Photo of a pole-mounted outdoor siren"></div>
    <div class="services">
      <h2 class="services-heading">Outdoor sirens</h2>
      <p class="services-lead">Notify people of severe dangers such as</p>
      <p class="services-list">Tornados <span class="sep">•</span>Severe thunderstorms <span class="sep">•</span>Flooding <span class="sep">•</span>Hurricanes <span class="sep">•</span>Tsunamis</p>
      <p class="services-lead">Oil and gas refining industries to warn of</p>
      <p class="services-list">Chemical releases <span class="sep">•</span>Fires <span class="sep">•</span>Lightning alerts</p>
    </div>
  </section>

</body>
</html>
```